Business Cards and Print Material
Business cards and print material
I like something that is out of the box. Something different and memorable. I will also need design for envelopes and letter heads. I like the designs so far. Please keep up the good work!
any info or ideas on what you would like ????

```html
<!DOCTYPE html>
<html lang="en">
<head>
<meta charset="utf-8">
<title>Halden Group – Letterhead and Business Cards</title>
<link rel="stylesheet" href="https://fonts.googleapis.com/css2?family=Cormorant+Garamond:wght@400;600&display=swap">
<style>
  :root {
    --backdrop: #e8e5e0;
    --navy-deep: #0d2459;
    --navy: #1d3f86;
    --navy-light: #3564b3;
    --paper: #ffffff;
    --ink-light: #e6ecf8;
    --ink-soft: #b9c8e6;
    --footer-ink: #27457f;
  }
  * { margin: 0; padding: 0; box-sizing: border-box; }
  html, body { width: 1200px; height: 871px; overflow: hidden; }
  body {
    background: var(--backdrop);
    font-family: "Cormorant Garamond", Georgia, serif;
    position: relative;
  }

  /* Letterhead */
  .letterhead {
    position: absolute;
    left: 90px; top: 40px;
    width: 560px; height: 792px;
    background: var(--paper);
    box-shadow: 0 4px 18px rgba(0,0,0,.18);
    overflow: hidden;
  }
  .letterhead-field {
    position: absolute;
    inset: 0 0 64px 0;
    background: linear-gradient(160deg, var(--navy-light) 0%, var(--navy) 45%, var(--navy-deep) 100%);
  }
  .brand {
    display: flex; align-items: center; gap: 10px;
    color: var(--paper);
    font-weight: 600;
    letter-spacing: .08em;
  }
  .brand-dot {
    width: 12px; height: 12px; border-radius: 50%;
    background: var(--paper);
  }
  .letterhead .brand {
    position: absolute; top: 56px; left: 0; right: 0;
    justify-content: center;
    font-size: 34px;
  }
  .letter-body {
    position: absolute; top: 190px; left: 70px; right: 70px;
    color: var(--ink-light);
    font-size: 15.5px; line-height: 1.55;
  }
  .letter-body p { margin-bottom: 16px; }
  .letter-sign { margin-top: 40px; }
  .signer-name { font-weight: 600; color: var(--paper); margin-top: 36px; margin-bottom: 0 !important; }
  .signer-title { color: var(--ink-soft); }
  .letter-footer {
    position: absolute; left: 0; right: 0; bottom: 0; height: 64px;
    display: flex; align-items: center; justify-content: center;
    color: var(--footer-ink);
    font-size: 12.5px; letter-spacing: .04em;
  }

  /* Business cards */
  .business-card {
    position: absolute;
    width: 440px; height: 252px;
    background: linear-gradient(150deg, var(--navy-light) 0%, var(--navy) 50%, var(--navy-deep) 100%);
    box-shadow: 0 4px 14px rgba(0,0,0,.2);
    color: var(--ink-light);
    overflow: hidden;
  }
  .card-one { left: 710px; top: 170px; }
  .card-two { left: 710px; top: 460px; }
  .business-card .brand {
    position: absolute; top: 40px; left: 0; right: 0;
    justify-content: center; font-size: 26px;
  }
  .card-name {
    position: absolute; top: 104px; right: 32px;
    font-size: 21px; font-weight: 600; letter-spacing: .14em;
    font-variant: small-caps; color: var(--paper);
  }
  .card-title {
    position: absolute; top: 132px; right: 32px;
    font-size: 13px; color: var(--ink-soft);
  }
  .card-contact {
    position: absolute; left: 32px; bottom: 26px;
    font-size: 12px; line-height: 1.5;
  }
  .card-contact dt { display: inline-block; width: 44px; color: var(--ink-soft); }
  .card-contact dd { display: inline; }
  .card-address {
    position: absolute; right: 32px; bottom: 26px;
    font-size: 12px; line-height: 1.5; text-align: right;
  }
</style>
</head>
<body>

<section class="letterhead">
  <div class="letterhead-field"></div>
  <div class="brand"><span class="brand-dot"></span>Halden Group</div>
  <div class="letter-body">
    <p>Dear Ms Rowan,</p>
    <p>Thank you for meeting with our team last week. We were glad to hear about your plans for the coming season and we look forward to helping your group reach new clients. Our studio will send a full outline of the project within the next few days.</p>
    <p>Please let us know if you have any questions about timing, budget or next steps. We value your trust and will keep you informed at every stage of the work ahead.</p>
    <p class="letter-sign">Sincerely,</p>
    <p class="signer-name">Tessa Wilde</p>
    <p class="signer-title">Director of Operations</p>
  </div>
  <footer class="letter-footer">47 Larkspur Lane, Suite 9, Riverton, TX 70000 &nbsp;|&nbsp; 555 010 2234 &nbsp;|&nbsp; hello@haldengroup.com</footer>
</section>

<section class="business-card card-one">
  <div class="brand"><span class="brand-dot"></span>Halden Group</div>
  <div class="card-name">Tessa Wilde</div>
  <div class="card-title">Director of Operations</div>
  <dl class="card-contact">
    <div><dt>Phone</dt><dd>555 010 2234</dd></div>
    <div><dt>Fax</dt><dd>555 010 2235</dd></div>
    <div><dt>Email</dt><dd>tessa@haldengroup.com</dd></div>
  </dl>
  <div class="card-address">47 Larkspur Lane, Suite 9<br>Riverton, TX 70000</div>
</section>

<section class="business-card card-two">
  <div class="brand"><span class="brand-dot"></span>Halden Group</div>
  <div class="card-name">Tessa Wilde</div>
  <div class="card-title">Director of Operations</div>
  <dl class="card-contact">
    <div><dt>Phone</dt><dd>555 010 2234</dd></div>
    <div><dt>Fax</dt><dd>555 010 2235</dd></div>
    <div><dt>Email</dt><dd>tessa@haldengroup.com</dd></div>
  </dl>
  <div class="card-address">47 Larkspur Lane, Suite 9<br>Riverton, TX 70000</div>
</section>

</body>
</html>
```